Brook Lending Flyer

Hi I need a professional flyer promoting me and my company. I can give you ideas of what to say once I see the design.

Below is my personal information needed in the flyer.

D: 510-437-2286
F: 877-540-6613
E: dean@BrookLendingInc.example
W: www.BrookLendingInc.example

NMLS# 475263/3081657 DRE# 02768419/03591864
Brook Lending Inc. | 127 Elm Avenue Ste. K | Pleasanton, CA 94583

Also I want to communicate tht we are friendly, fast, transparent, we communicate clearly and often, we educate (we want to make sure the buyer understands everything). Our team had over 60+ years experience. We are the alternative to the big box banks. We provide concierge service every step of the way.
Experience #The BrookLendingDifference

"Brook Lending is committed to a simple, fast, hassle free and fum mortgage experience every time." President -Dean Brook

Veteran Owned Business

Target Market(s)

Home buyers

Industry/Entity Type

Mortgage

Font styles to use
Decorative

Colors
59FF00
82FF00
B8FF75
E3FFCB
F4FFEA
FFC000
F8CF3A
FAE287
FDF2CF
FEFAEE

Requirements
Must have
• Please make it look professional maybe with some curves or something. Look at other really professional flyers for ideas.
Nice to have
• Curves and a couple areas to discuss why Brook Lending and types of financing we do
Should not have
• I don't know

```html
<!DOCTYPE html>
<html lang="en">
<head>
<meta charset="utf-8">
<title>Brook Lending Flyer</title>
<link href="https://fonts.googleapis.com/css2?family=Ubuntu:wght@400;500;700&display=swap" rel="stylesheet">
<style>
  :root {
    --stage: #e4e4e4;
    --paper: #ffffff;
    --ink: #555555;
    --ink-dark: #4a4a4a;
    --orange: #f59a23;
    --amber: #ffc000;
    --yellow: #f6ec1e;
    --lime: #9dcb12;
    --lime-deep: #8cc21a;
    --photo-a: #5b4a3c;
    --photo-b: #22252d;
  }
  * { margin: 0; padding: 0; box-sizing: border-box; }
  html, body { width: 1200px; height: 1200px; overflow: hidden; background: var(--stage); }
  body { font-family: "Ubuntu", sans-serif; color: var(--ink); }

  .flyer {
    position: absolute; left: 190px; top: 20px;
    width: 820px; height: 1160px;
    background: var(--paper);
    overflow: hidden;
    box-shadow: 0 6px 18px rgba(0,0,0,.18);
  }
  .bands { position: absolute; inset: 0; width: 820px; height: 1160px; }

  .brand {
    position: absolute; left: 70px; top: 90px;
    display: flex; align-items: center; gap: 12px;
  }
  .brand-dot { width: 22px; height: 22px; border-radius: 50%; background: var(--lime); }
  .brand-name { font-size: 38px; font-weight: 700; color: var(--ink-dark); letter-spacing: .5px; }

  .why { position: absolute; left: 70px; top: 330px; width: 390px; }
  .section-title { font-weight: 700; color: var(--ink); }
  .why .section-title { font-size: 32px; margin-bottom: 18px; }
  .why p { font-size: 13.5px; font-weight: 500; line-height: 1.42; color: var(--ink-dark); margin-bottom: 16px; }

  .portrait-frame {
    position: absolute; left: 480px; top: 300px;
    width: 320px; height: 400px;
    border-radius: 46% 46% 44% 44% / 40% 40% 48% 48%;
    background: linear-gradient(150deg, var(--yellow), var(--lime) 60%, var(--lime-deep));
    transform: rotate(-8deg);
  }
  .portrait {
    position: absolute; left: 14px; top: 14px; right: 18px; bottom: 20px;
    border-radius: 46% 46% 44% 44% / 40% 40% 48% 48%;
    background: linear-gradient(160deg, #c9b9a2 0%, var(--photo-a) 40%, var(--photo-b) 80%);
  }

  .financing { position: absolute; left: 70px; top: 712px; }
  .financing .section-title { font-size: 36px; margin-bottom: 18px; }
  .financing ul { list-style: none; }
  .financing li {
    display: flex; align-items: center; gap: 18px;
    font-size: 19px; font-weight: 500; color: var(--ink-dark);
    margin-bottom: 9px;
  }
  .tick { width: 22px; height: 20px; flex: none; }

  .phone {
    position: absolute; left: 80px; top: 1060px;
    display: flex; align-items: center; gap: 30px;
    font-size: 44px; font-weight: 700; color: var(--ink-dark);
  }
  .phone svg { width: 46px; height: 46px; }

  .contact {
    position: absolute; right: 40px; top: 1000px;
    text-align: right; font-size: 16px; font-style: normal; color: var(--ink-dark);
  }
  .contact-row { display: flex; justify-content: flex-end; align-items: flex-start; gap: 16px; margin-bottom: 6px; line-height: 1.25; }
  .contact-row svg { width: 22px; height: 22px; flex: none; }
</style>
</head>
<body>
<main class="flyer">
  <svg class="bands" viewBox="0 0 820 1160" aria-hidden="true">
    <defs>
      <linearGradient id="cornerBand" x1="0" y1="0" x2="1" y2="0">
        <stop offset="0" stop-color="#ffc000"/>
        <stop offset=".6" stop-color="#f59a23"/>
        <stop offset="1" stop-color="#9dcb12"/>
      </linearGradient>
      <linearGradient id="footBand" x1="0" y1="0" x2="1" y2="0">
        <stop offset="0" stop-color="#f8ee20"/>
        <stop offset=".6" stop-color="#d2dc0c"/>
        <stop offset="1" stop-color="#94c81a"/>
      </linearGradient>
    </defs>
    <path d="M820 0 H520 C480 170 640 250 820 270 Z" fill="url(#cornerBand)"/>
    <path d="M0 1010 Q 500 1020 820 860 V1160 H0 Z" fill="url(#footBand)"/>
  </svg>

  <div class="brand">
    <span class="brand-dot"></span>
    <span class="brand-name">Brook Lending</span>
  </div>

  <section class="why">
    <h2 class="section-title">Why Brook Lending</h2>
    <p>Lorem ipsum dolor sit amet, consectetur adipiscing elit. Fusce aliquet sodales sapien. Maecenas id egestas sem. Aliquam massa diam, tincidunt ac enim sed, vulputate tincidunt nisl. Vivamus molestie elementum odio, nec laoreet sapien. Quisque vel dignissim nulla, non porttitor massa. Sed vitae neque ex. In semper lacus nibh, vitae vulputate ligula efficitur sit amet. Donec non justo diam. Morbi cursus dolor vel erat bibendum, feugiat luctus quam tempus. Nulla id imperdiet augue.</p>
    <p>Quisque vel neque scelerisque tellus ullamcorper semper. Maecenas laoreet, turpis at finibus ultricies, neque velit consequat nisl, eu scelerisque sem sem nec augue. Nunc id sem bibendum quam varius euismod eget ut elit. Suspendisse potenti. Sed dignissim elit lacus, id commodo nunc vestibulum vitae. Nulla bibendum quis purus quis pharetra.</p>
  </section>

  <div class="portrait-frame">
    <div class="portrait" role="img" aria-label="Portrait photo of the company president in a dark suit"></div>
  </div>

  <section class="financing">
    <h2 class="section-title">Types of Financing We Do</h2>
    <ul>
      <li><svg class="tick" viewBox="0 0 22 20"><rect x="1.5" y="5" width="14" height="13" fill="none" stroke="#ffc000" stroke-width="2"/><path d="M5 11 L9 15 L20 2" fill="none" stroke="#f59a23" stroke-width="2.5"/></svg>Lorem ipsum dolor sit amet, consectetur adipiscing elit.</li>
      <li><svg class="tick" viewBox="0 0 22 20"><rect x="1.5" y="5" width="14" height="13" fill="none" stroke="#ffc000" stroke-width="2"/><path d="M5 11 L9 15 L20 2" fill="none" stroke="#f59a23" stroke-width="2.5"/></svg>Curabitur in elit eget purus volutpat mattis.</li>
      <li><svg class="tick" viewBox="0 0 22 20"><rect x="1.5" y="5" width="14" height="13" fill="none" stroke="#ffc000" stroke-width="2"/><path d="M5 11 L9 15 L20 2" fill="none" stroke="#f59a23" stroke-width="2.5"/></svg>Vestibulum venenatis metus non vulputate congue.</li>
      <li><svg class="tick" viewBox="0 0 22 20"><rect x="1.5" y="5" width="14" height="13" fill="none" stroke="#ffc000" stroke-width="2"/><path d="M5 11 L9 15 L20 2" fill="none" stroke="#f59a23" stroke-width="2.5"/></svg>Etiam et lorem consequat, interdum ante sit amet.</li>
      <li><svg class="tick" viewBox="0 0 22 20"><rect x="1.5" y="5" width="14" height="13" fill="none" stroke="#ffc000" stroke-width="2"/><path d="M5 11 L9 15 L20 2" fill="none" stroke="#f59a23" stroke-width="2.5"/></svg>Morbi at ex sed libero tempus feugiat.</li>
    </ul>
  </section>

  <div class="phone">
    <svg viewBox="0 0 24 24"><path fill="#555" d="M6.6 10.8c1.4 2.8 3.8 5.1 6.6 6.6l2.2-2.2c.3-.3.7-.4 1-.2 1.1.4 2.3.6 3.6.6.6 0 1 .4 1 1V20c0 .6-.4 1-1 1C10.6 21 3 13.4 3 4c0-.6.4-1 1-1h3.5c.6 0 1 .4 1 1 0 1.3.2 2.5.6 3.6.1.3 0 .7-.2 1z"/></svg>
    <span>+ 9999 1234 000</span>
  </div>

  <address class="contact">
    <div class="contact-row"><span>Lorem ipsum adipiscing elit dolor sit amet<br>consectetur adipiscing elit</span>
      <svg viewBox="0 0 24 24"><path fill="#555" d="M12 2a7 7 0 0 0-7 7c0 5 7 13 7 13s7-8 7-13a7 7 0 0 0-7-7zm0 9.5A2.5 2.5 0 1 1 12 6.5a2.5 2.5 0 0 1 0 5z"/></svg></div>
    <div class="contact-row"><span>enquiry@brooklending.example</span>
      <svg viewBox="0 0 24 24"><rect x="2" y="5" width="20" height="14" fill="#555"/><path d="M2 5 L12 13 L22 5" fill="none" stroke="#fff" stroke-width="1.5"/></svg></div>
    <div class="contact-row"><span>www.brooklending.example</span>
      <svg viewBox="0 0 24 24" fill="none" stroke="#555" stroke-width="1.6"><circle cx="12" cy="12" r="9"/><ellipse cx="12" cy="12" rx="4" ry="9"/><path d="M3 12h18M5 7h14M5 17h14"/></svg></div>
  </address>
</main>
</body>
</html>
```